Sunny Nibble Snack Drops

Hello! I need the attached pdf artwork of individual pouch designs to be fit into both attached templates in a CYMK format. Each design/ flavor needs to be fit into the individual pouch template and the sea end box template. I need to artwork files to send to printing. Thank you!

Target Market(s)

Everyone who loves yummy snacks.

Font styles to use
Script
Other font styles liked:
• See attached design.

Colors

Designer to choose colors to be used in the design.

Requirements
Must have
• Designs must fit attached templates, bleed areas, be in the correct format, etc. The tan areas on the side if the packages are a place holder for the kraft material the design will be printed on. The box template design and individual pouch template need to be cohesive.
Nice to have
• Think Mork Pop but brighter,
Should not have
• Designs cannot be made to not fit the attached templates.

```html
<!DOCTYPE html>
<html lang="en">
<head>
<meta charset="utf-8">
<title>Sunny Nibble Snack Drops – Pouch Flavours</title>
<link href="https://fonts.googleapis.com/css2?family=Cutive+Mono&family=Roboto:wght@400;700&display=swap" rel="stylesheet">
<style>
  :root {
    --kraft: #fbe1d6;
    --paper: #ffffff;
    --ink: #222222;
    --page: #ffffff;
    --chip: #1fc1ef;
    --maple: #f3736b;
    --seasalt: #f36fb0;
    --nut: #8ccd73;
    --pbj: #7a6fb3;
    --coconut: #f05a48;
    --mono: "Cutive Mono", "Courier New", monospace;
    --sans: "Roboto", Arial, sans-serif;
  }
  * { margin: 0; padding: 0; box-sizing: border-box; }
  html, body { width: 1200px; height: 683px; overflow: hidden; background: var(--page); }
  .sheet { position: relative; width: 1200px; height: 683px; }

  .pouch {
    position: absolute; width: 502px; height: 165px;
    background: var(--kraft);
    box-shadow: 8px 8px 10px rgba(0,0,0,.35);
    color: var(--paper);
  }
  .pouch--chip    { --flavor: var(--chip);    left: 55px;  top: 30px; }
  .pouch--maple   { --flavor: var(--maple);   left: 644px; top: 30px; }
  .pouch--seasalt { --flavor: var(--seasalt); left: 53px;  top: 250px; }
  .pouch--nut     { --flavor: var(--nut);     left: 644px; top: 250px; }
  .pouch--pbj     { --flavor: var(--pbj);     left: 55px;  top: 483px; }
  .pouch--coconut { --flavor: var(--coconut); left: 644px; top: 483px; }

  /* reads bottom-to-top: anchor = bottom-left corner of the turned box */
  .up { position: absolute; transform-origin: 0 0; transform: rotate(-90deg); white-space: nowrap; }
  /* reads top-to-bottom: anchor = top-right corner of the turned box */
  .down { position: absolute; transform-origin: 0 0; transform: rotate(90deg); }

  .front { position: absolute; left: 0; top: 12px; width: 217px; height: 141px; background: var(--flavor); overflow: hidden; }
  .front__claims { left: 4px; top: 132px; width: 126px; height: 18px; font: 6.6px/8px var(--mono); }
  .front__badge { position: absolute; left: 58px; top: 27px; width: 86px; height: 86px; }
  .front__brand { left: 91px; top: 105px; width: 70px; height: 20px; font: 8.4px/10px var(--mono); text-align: center; }
  .front__slogan { left: 152px; top: 131px; width: 126px; height: 14px; font: 8.6px/14px var(--mono); }
  .front__flavor { left: 175px; top: 130px; width: 120px; height: 10px; font: 6px/10px var(--sans); text-align: center; }
  .front__weight { left: 205px; top: 84px; width: 80px; height: 7px; font: 4.4px/7px var(--sans); }

  .gusset { color: var(--ink); font: 4.6px/6px var(--sans); text-align: center; }
  .gusset__origin { left: 229px; top: 115px; width: 70px; height: 14px; }
  .gusset__maker { left: 261px; top: 127px; width: 90px; height: 14px; }

  .back { position: absolute; left: 284px; top: 12px; width: 218px; height: 141px; background: var(--flavor); overflow: hidden; }
  .back__flavor { left: 210px; top: 10px; width: 120px; height: 10px; font: 6px/10px var(--sans); text-align: center; white-space: nowrap; }
  .label { position: absolute; left: 11px; top: 1px; width: 161px; height: 139px; background: var(--paper); color: var(--ink); overflow: hidden; }
  .label__title { left: 157px; top: 2px; width: 135px; height: 11px; font: 400 7px/11px var(--mono); white-space: nowrap; font-weight: 700; }
  .label__story { left: 142px; top: 5px; width: 80px; height: 140px; font: 3.5px/4.3px var(--sans); }
  .label__story p { margin-bottom: 2px; }
  .label__story ul { list-style: none; padding-left: 10px; margin-bottom: 3px; }
  .label__story li::before { content: "◆ "; font-size: 3px; }

  .facts { left: 144px; top: 86px; width: 44px; height: 89px; border: .6px solid var(--ink); padding: 1px; font: 2.8px/3.4px var(--sans); white-space: nowrap; overflow: hidden; }
  .facts__row { border-bottom: .4px solid var(--ink); }
  .facts__head { font-weight: 700; font-size: 4.6px; line-height: 5.6px; border-bottom-width: 1.6px; }
  .facts__cal { font-weight: 700; font-size: 3.6px; line-height: 4.6px; border-bottom-width: 1.2px; }
  .ingredients { left: 53px; top: 86px; width: 44px; height: 17px; font: 2.6px/3.4px var(--sans); }
</style>
</head>
<body>
<main class="sheet">

  <article class="pouch pouch--chip">
    <section class="front">
      <p class="up front__claims">No artificial flavorings.<br>No added sugar. No funny stuff.</p>
      <svg class="front__badge" viewBox="0 0 86 86" aria-hidden="true"><circle cx="43" cy="43" r="40" fill="none" stroke="#ffffff" stroke-opacity=".5" stroke-width="3"/></svg>
      <p class="up front__brand">Sunny Nibble<br>Snack Drops</p>
      <p class="up front__slogan">Always the perfect bite.</p>
      <p class="up front__flavor">Chocolate Chip</p>
      <p class="up front__weight">Net weight 1.8 oz. (51g) per pack</p>
    </section>
    <p class="up gusset gusset__origin">Made in the USA<br>BEST BY</p>
    <p class="up gusset gusset__maker">Manufactured by Mira Calloway LLC<br>Palmview, FL 30417</p>
    <section class="back">
      <p class="down back__flavor">Chocolate Chip</p>
      <div class="label">
        <h2 class="down label__title">Take a Sunny Nibble out of life!</h2>
        <div class="down label__story">
          <p>Sunny Nibbles were made for me and for you. Fed up with long ingredient labels, my goal was to create a delicious snack made with high quality ingredients and no funny stuff.</p>
          <p>Sunny Nibbles are that snack. Made with real and nutritious ingredients, they satisfy your sweet tooth without busting your belt. Take them on a run, eat them at your desk, do whatever you need them to do. They're made for you.</p>
          <p>So, here's to good food that's also good for you. I hope you enjoy them as much as I do and thank you for giving them a try.</p>
          <ul><li>No artificial flavorings</li><li>No added sugar</li><li>No funny stuff</li></ul>
          <p>Mira</p>
          <p>www.sunnynibblesbymira.com</p>
        </div>
        <div class="down facts">
          <div class="facts__row facts__head">Nutrition Facts</div>
          <div class="facts__row">Serving size 1 pack (51g)</div>
          <div class="facts__row facts__cal">Calories 190</div>
          <div class="facts__row">Total Fat 9g 12%</div>
          <div class="facts__row">Sodium 60mg 3%</div>
          <div class="facts__row">Total Carb. 22g 8%</div>
          <div class="facts__row">Protein 5g</div>
        </div>
        <p class="down ingredients">Ingredients: oats, dates, almond butter, cocoa, sea salt. Contains: tree nuts.</p>
      </div>
    </section>
  </article>

  <article class="pouch pouch--maple">
    <section class="front">
      <p class="up front__claims">No artificial flavorings.<br>No additives. No funny stuff.</p>
      <svg class="front__badge" viewBox="0 0 86 86" aria-hidden="true"><circle cx="43" cy="43" r="40" fill="none" stroke="#ffffff" stroke-opacity=".5" stroke-width="3"/></svg>
      <p class="up front__brand">Sunny Nibble<br>Snack Drops</p>
      <p class="up front__slogan">Always the perfect bite.</p>
      <p class="up front__flavor">Maple Cinnamon</p>
      <p class="up front__weight">Net weight 1.8 oz. (51g) per pack</p>
    </section>
    <p class="up gusset gusset__origin">Made in the USA<br>BEST BY</p>
    <p class="up gusset gusset__maker">Manufactured by Mira Calloway LLC<br>Palmview, FL 30417</p>
    <section class="back">
      <p class="down back__flavor">Maple Cinnamon</p>
      <div class="label">
        <h2 class="down label__title">Take a Sunny Nibble out of life!</h2>
        <div class="down label__story">
          <p>Sunny Nibbles were made for me and for you. Fed up with long ingredient labels, my goal was to create a delicious snack made with high quality ingredients and no funny stuff.</p>
          <p>Sunny Nibbles are that snack. Made with real and nutritious ingredients, they satisfy your sweet tooth without busting your belt. Take them on a run, eat them at your desk, do whatever you need them to do. They're made for you.</p>
          <p>So, here's to good food that's also good for you. I hope you enjoy them as much as I do and thank you for giving them a try.</p>
          <ul><li>No artificial flavorings</li><li>No added sugar</li><li>No funny stuff</li></ul>
          <p>Mira</p>
          <p>www.sunnynibblesbymira.com</p>
        </div>
        <div class="down facts">
          <div class="facts__row facts__head">Nutrition Facts</div>
          <div class="facts__row">Serving size 1 pack (51g)</div>
          <div class="facts__row facts__cal">Calories 190</div>
          <div class="facts__row">Total Fat 9g 12%</div>
          <div class="facts__row">Sodium 60mg 3%</div>
          <div class="facts__row">Total Carb. 22g 8%</div>
          <div class="facts__row">Protein 5g</div>
        </div>
        <p class="down ingredients">Ingredients: oats, dates, almond butter, cocoa, sea salt. Contains: tree nuts.</p>
      </div>
    </section>
  </article>

  <article class="pouch pouch--seasalt">
    <section class="front">
      <p class="up front__claims">No artificial flavorings.<br>No added sugar. No funny stuff.</p>
      <svg class="front__badge" viewBox="0 0 86 86" aria-hidden="true"><circle cx="43" cy="43" r="40" fill="none" stroke="#ffffff" stroke-opacity=".5" stroke-width="3"/></svg>
      <p class="up front__brand">Sunny Nibble<br>Snack Drops</p>
      <p class="up front__slogan">Always the perfect bite.</p>
      <p class="up front__flavor">Dark Chocolate Sea Salt</p>
      <p class="up front__weight">Net weight 1.8 oz. (51g) per pack</p>
    </section>
    <p class="up gusset gusset__origin">Made in the USA<br>BEST BY</p>
    <p class="up gusset gusset__maker">Manufactured by Mira Calloway LLC<br>Palmview, FL 30417</p>
    <section class="back">
      <p class="down back__flavor">Dark Chocolate Sea Salt</p>
      <div class="label">
        <h2 class="down label__title">Take a Sunny Nibble out of life!</h2>
        <div class="down label__story">
          <p>Sunny Nibbles were made for me and for you. Fed up with long ingredient labels, my goal was to create a delicious snack made with high quality ingredients and no funny stuff.</p>
          <p>Sunny Nibbles are that snack. Made with real and nutritious ingredients, they satisfy your sweet tooth without busting your belt. Take them on a run, eat them at your desk, do whatever you need them to do. They're made for you.</p>
          <p>So, here's to good food that's also good for you. I hope you enjoy them as much as I do and thank you for giving them a try.</p>
          <ul><li>No artificial flavorings</li><li>No added sugar</li><li>No funny stuff</li></ul>
          <p>Mira</p>
          <p>www.sunnynibblesbymira.com</p>
        </div>
        <div class="down facts">
          <div class="facts__row facts__head">Nutrition Facts</div>
          <div class="facts__row">Serving size 1 pack (51g)</div>
          <div class="facts__row facts__cal">Calories 190</div>
          <div class="facts__row">Total Fat 9g 12%</div>
          <div class="facts__row">Sodium 60mg 3%</div>
          <div class="facts__row">Total Carb. 22g 8%</div>
          <div class="facts__row">Protein 5g</div>
        </div>
        <p class="down ingredients">Ingredients: oats, dates, almond butter, cocoa, sea salt. Contains: tree nuts.</p>
      </div>
    </section>
  </article>

  <article class="pouch pouch--nut">
    <section class="front">
      <p class="up front__claims">No artificial flavorings.<br>No additives. No funny stuff.</p>
      <svg class="front__badge" viewBox="0 0 86 86" aria-hidden="true"><circle cx="43" cy="43" r="40" fill="none" stroke="#ffffff" stroke-opacity=".5" stroke-width="3"/></svg>
      <p class="up front__brand">Sunny Nibble<br>Snack Drops</p>
      <p class="up front__slogan">Always the perfect bite.</p>
      <p class="up front__flavor">Health Nut</p>
      <p class="up front__weight">Net weight 1.8 oz. (51g) per pack</p>
    </section>
    <p class="up gusset gusset__origin">Made in the USA<br>BEST BY</p>
    <p class="up gusset gusset__maker">Manufactured by Mira Calloway LLC<br>Palmview, FL 30417</p>
    <section class="back">
      <p class="down back__flavor">Health Nut</p>
      <div class="label">
        <h2 class="down label__title">Take a Sunny Nibble out of life!</h2>
        <div class="down label__story">
          <p>Sunny Nibbles were made for me and for you. Fed up with long ingredient labels, my goal was to create a delicious snack made with high quality ingredients and no funny stuff.</p>
          <p>Sunny Nibbles are that snack. Made with real and nutritious ingredients, they satisfy your sweet tooth without busting your belt. Take them on a run, eat them at your desk, do whatever you need them to do. They're made for you.</p>
          <p>So, here's to good food that's also good for you. I hope you enjoy them as much as I do and thank you for giving them a try.</p>
          <ul><li>No artificial flavorings</li><li>No added sugar</li><li>No funny stuff</li></ul>
          <p>Mira</p>
          <p>www.sunnynibblesbymira.com</p>
        </div>
        <div class="down facts">
          <div class="facts__row facts__head">Nutrition Facts</div>
          <div class="facts__row">Serving size 1 pack (51g)</div>
          <div class="facts__row facts__cal">Calories 190</div>
          <div class="facts__row">Total Fat 9g 12%</div>
          <div class="facts__row">Sodium 60mg 3%</div>
          <div class="facts__row">Total Carb. 22g 8%</div>
          <div class="facts__row">Protein 5g</div>
        </div>
        <p class="down ingredients">Ingredients: oats, dates, almond butter, cocoa, sea salt. Contains: tree nuts.</p>
      </div>
    </section>
  </article>

  <article class="pouch pouch--pbj">
    <section class="front">
      <p class="up front__claims">No artificial flavorings.<br>No additives. No funny stuff.</p>
      <svg class="front__badge" viewBox="0 0 86 86" aria-hidden="true"><circle cx="43" cy="43" r="40" fill="none" stroke="#ffffff" stroke-opacity=".5" stroke-width="3"/></svg>
      <p class="up front__brand">Sunny Nibble<br>Snack Drops</p>
      <p class="up front__slogan">Always the perfect bite.</p>
      <p class="up front__flavor">Peanut Butter &amp; Jelly</p>
      <p class="up front__weight">Net weight 1.8 oz. (51g) per pack</p>
    </section>
    <p class="up gusset gusset__origin">Made in the USA<br>BEST BY</p>
    <p class="up gusset gusset__maker">Manufactured by Mira Calloway LLC<br>Palmview, FL 30417</p>
    <section class="back">
      <p class="down back__flavor">Peanut Butter &amp; Jelly</p>
      <div class="label">
        <h2 class="down label__title">Take a Sunny Nibble out of life!</h2>
        <div class="down label__story">
          <p>Sunny Nibbles were made for me and for you. Fed up with long ingredient labels, my goal was to create a delicious snack made with high quality ingredients and no funny stuff.</p>
          <p>Sunny Nibbles are that snack. Made with real and nutritious ingredients, they satisfy your sweet tooth without busting your belt. Take them on a run, eat them at your desk, do whatever you need them to do. They're made for you.</p>
          <p>So, here's to good food that's also good for you. I hope you enjoy them as much as I do and thank you for giving them a try.</p>
          <ul><li>No artificial flavorings</li><li>No added sugar</li><li>No funny stuff</li></ul>
          <p>Mira</p>
          <p>www.sunnynibblesbymira.com</p>
        </div>
        <div class="down facts">
          <div class="facts__row facts__head">Nutrition Facts</div>
          <div class="facts__row">Serving size 1 pack (51g)</div>
          <div class="facts__row facts__cal">Calories 190</div>
          <div class="facts__row">Total Fat 9g 12%</div>
          <div class="facts__row">Sodium 60mg 3%</div>
          <div class="facts__row">Total Carb. 22g 8%</div>
          <div class="facts__row">Protein 5g</div>
        </div>
        <p class="down ingredients">Ingredients: oats, dates, almond butter, cocoa, sea salt. Contains: tree nuts.</p>
      </div>
    </section>
  </article>

  <article class="pouch pouch--coconut">
    <section class="front">
      <p class="up front__claims">No artificial flavorings.<br>No additives. No funny stuff.</p>
      <svg class="front__badge" viewBox="0 0 86 86" aria-hidden="true"><circle cx="43" cy="43" r="40" fill="none" stroke="#ffffff" stroke-opacity=".5" stroke-width="3"/></svg>
      <p class="up front__brand">Sunny Nibble<br>Snack Drops</p>
      <p class="up front__slogan">Always the perfect bite.</p>
      <p class="up front__flavor">Strawberry Chocolate Coconut</p>
      <p class="up front__weight">Net weight 1.8 oz. (51g) per pack</p>
    </section>
    <p class="up gusset gusset__origin">Made in the USA<br>BEST BY</p>
    <p class="up gusset gusset__maker">Manufactured by Mira Calloway LLC<br>Palmview, FL 30417</p>
    <section class="back">
      <p class="down back__flavor">Strawberry Chocolate Coconut</p>
      <div class="label">
        <h2 class="down label__title">Take a Sunny Nibble out of life!</h2>
        <div class="down label__story">
          <p>Sunny Nibbles were made for me and for you. Fed up with long ingredient labels, my goal was to create a delicious snack made with high quality ingredients and no funny stuff.</p>
          <p>Sunny Nibbles are that snack. Made with real and nutritious ingredients, they satisfy your sweet tooth without busting your belt. Take them on a run, eat them at your desk, do whatever you need them to do. They're made for you.</p>
          <p>So, here's to good food that's also good for you. I hope you enjoy them as much as I do and thank you for giving them a try.</p>
          <ul><li>No artificial flavorings</li><li>No added sugar</li><li>No funny stuff</li></ul>
          <p>Mira</p>
          <p>www.sunnynibblesbymira.com</p>
        </div>
        <div class="down facts">
          <div class="facts__row facts__head">Nutrition Facts</div>
          <div class="facts__row">Serving size 1 pack (51g)</div>
          <div class="facts__row facts__cal">Calories 190</div>
          <div class="facts__row">Total Fat 9g 12%</div>
          <div class="facts__row">Sodium 60mg 3%</div>
          <div class="facts__row">Total Carb. 22g 8%</div>
          <div class="facts__row">Protein 5g</div>
        </div>
        <p class="down ingredients">Ingredients: oats, dates, almond butter, cocoa, sea salt. Contains: tree nuts.</p>
      </div>
    </section>
  </article>

</main>
</body>
</html>
```